Website Design - for Energy Efficiency company - large corporate feel

Hi there,
Thanks for checking out this project!
We're a UK based energy efficiency business. We arrange for energy efficient systems to be fitted in people's houses (i.e. efficient boilers, solar panels etc.) However, we do not install them ourselves as we have accredited installers who install on our behalf. Therefore the website should appeal to these businesses and have a very professional corporate feel. The final design should communicate that we are a financially safe large corporation.
Our existing website should not be used for inspiration as the style and content are very outdated (it was from a time when were installers - which we no longer are).
The new website design should use the greens from our logo, however I don't want the site saturated in this colour.
I'm really open to your chosen layout and therefore I'm not a huge fan of including links to websites I like - as I don't want to limit your own creativity. However, I would like it to look corporate (but not too boring and unimaginative).
So here's a few links to websites that I feel give a feel of financially safe / large corporate etc. Although you certainly don't have to design with this style / layout in mind:
http://www.brelvanhub.org.uk/advice
http://www.tolvenrise.co.uk/
http://www.qpwd.org.uk/
http://www.wendrowkeyplot.co.uk/
http://www.ruvasto.co.uk/ (very bad design but looks corporate)
http://www.pellarwatt.org.uk/
http://www.vq.co.uk/ (looks corporate but too busy and boring)
http://www.quellisto.co.uk/business/index.htm
http://www.dormavel.com/
https://www.ostrevan.com/en/index.html
The site is for 4 different audiences:
Consumers | Businesses | Public Sector | Installers
Therefore, it's important that there is some form of way of splitting the site up into these sections (almost like 4 websites in 1). Each section will then have the navigation menu with 7 links.
I've attached our logo (company-logo.jpg) and another logo design we have to display inline with regulations (blue-pact-logo.jpg).
Happy designing, and thank you!

```html
<!DOCTYPE html>
<html lang="en">
<head>
<meta charset="utf-8">
<title>Leafmore Energy</title>
<link href="https://fonts.googleapis.com/css2?family=Open+Sans:wght@400;600;700&display=swap" rel="stylesheet">
<style>
:root{
  --field:#5f9a2c;
  --field-dark:#4a8020;
  --paper:#ffffff;
  --leaf:#4e8a1e;
  --leaf-bright:#7cb833;
  --nav-top:#7fb93a;
  --nav-bottom:#5d9a22;
  --ink:#555a5e;
  --ink-soft:#777b7f;
  --slate:#4b5966;
  --amber:#b8730f;
  --moss:#6f9a3e;
  --steel:#3f4d5c;
  --gold:#d8a918;
  --band:#f1f1f1;
  --footer:#2f5212;
  --btn:#56636f;
}
*{box-sizing:border-box;margin:0;padding:0}
html,body{width:886px;height:1200px;overflow:hidden}
body{
  font-family:"Open Sans",Arial,sans-serif;
  background:radial-gradient(ellipse at 50% 40%,#86bd4c 0%,var(--field) 55%,var(--field-dark) 100%);
  color:var(--ink);
  position:relative;
}
.page{position:absolute;left:116px;top:0;width:650px;height:1200px;background:var(--paper);box-shadow:0 0 14px rgba(0,0,0,.35)}
.abs{position:absolute}

/* header */
.brand{left:22px;top:30px;display:flex;align-items:center;gap:6px}
.brand-dot{width:30px;height:30px;border-radius:50%;background:var(--leaf)}
.brand-name{font-size:24px;font-weight:700;color:var(--leaf);letter-spacing:-.5px;line-height:1}
.social{left:410px;top:34px;display:flex;gap:5px;align-items:center}
.social span{width:24px;height:24px;border-radius:50%;display:block}
.social .s1{background:#2f9ad6}.social .s2{background:#e36a2a}.social .s3{background:#3f74c4}
.social .divider{width:1px;height:10px;background:#b9cf5a;border-radius:0;margin-left:6px}
.search{left:517px;top:34px;width:113px;height:25px;border:1px solid #b9cf77;border-radius:2px;font-size:10px;color:#777;padding:5px 7px}
.search svg{position:absolute;right:6px;top:6px}

/* nav */
.nav{left:20px;top:78px;width:611px;height:35px;display:flex;background:linear-gradient(var(--nav-top),var(--nav-bottom));border-radius:2px}
.nav a{color:#fff;text-decoration:none;font-size:10.5px;display:flex;align-items:center;justify-content:center;border-right:1px solid rgba(0,0,0,.15);text-transform:uppercase}
.nav a.active{background:#93c84d}
.nav a:last-child{border-right:0}

/* hero */
.hero{left:20px;top:126px;width:611px;height:260px;background:linear-gradient(160deg,#9aa7b3 0%,#7a8794 35%,#5a5f63 60%,#2b3a55 100%)}
.hero h1{position:absolute;left:46px;top:34px;font-weight:400;font-size:22px;color:#2c2f31}
.hero h1 em{font-style:normal;color:var(--leaf)}
.hero p{position:absolute;left:46px;top:69px;font-size:11px;line-height:15px;color:#3d4347}
.hero .join{position:absolute;left:46px;top:110px;width:89px;height:25px;background:var(--btn);color:#fff;font-size:11px;font-weight:600;display:flex;align-items:center;justify-content:center;border-radius:2px}

/* audiences */
.audiences{left:20px;top:386px;width:611px;height:121px;display:flex}
.aud{flex:1;text-align:center;color:#fff;padding-top:17px}
.aud h3{font-size:12.5px;font-weight:400;text-transform:uppercase}
.aud p{font-size:8.5px;line-height:10.5px;margin:6px auto 0;width:125px;opacity:.9}
.aud .details{display:inline-block;margin-top:11px;border:1px solid rgba(255,255,255,.8);font-size:8.5px;font-weight:600;padding:5px 10px}
.consumers{background:linear-gradient(var(--amber),#a2640c)}
.businesses{background:linear-gradient(var(--moss),#5f8a32)}
.public{background:linear-gradient(var(--steel),#36424f)}
.installers{background:linear-gradient(var(--gold),#c89c10)}

/* section titles */
.section-title{left:85px;width:476px;display:flex;align-items:center;gap:10px;font-size:13px;color:var(--leaf);text-transform:uppercase}
.section-title::before,.section-title::after{content:"";flex:1;border-top:1px dashed #c8c8c8}

.about-badge{left:99px;top:570px}
.about-text{left:164px;top:567px;width:380px;font-size:8.6px;line-height:13px;color:var(--ink-soft)}

/* products */
.products{left:0;top:656px;width:650px;height:252px;background:var(--band)}
.arrow{font-size:18px;color:#999}
.product{width:144px}
.product h4{font-size:11px;font-weight:400;color:var(--leaf)}
.product .thumb{margin-top:6px;width:144px;height:75px;border:1px solid #ddd;background:#fff;padding:5px}
.product .thumb div{width:100%;height:100%}
.product p{margin-top:13px;font-size:8.4px;line-height:10.5px;color:var(--ink)}
.product .more{display:inline-block;margin-top:13px;background:var(--btn);color:#fff;font-size:8.5px;font-weight:600;padding:4px 10px;border-radius:1px}

/* testimonials & contact */
.block-title{font-size:13px;color:#4a4e52;font-weight:400;text-transform:uppercase}
.block-title em{font-style:normal;color:var(--leaf)}
.avatar{left:89px;top:962px;width:78px;height:78px;border-radius:50%;background:linear-gradient(#e9eef1,#9aa3aa);border:3px solid #e6e6e6}
.who{left:182px;top:980px;font-size:8.6px;line-height:13px;font-style:italic;color:var(--ink-soft)}
.who b{font-weight:400;color:var(--leaf)}
.quote{left:91px;top:1048px;width:215px;font-size:8.6px;line-height:13px;color:var(--ink-soft)}
.field{left:349px;width:191px;border:1px solid #cfcfcf;font-size:8.6px;color:#555;padding:5px 7px;background:#fff}
.submit{left:349px;top:1078px;width:60px;height:23px;background:linear-gradient(#3f8a1a,#2d6d0e);color:#fff;font-size:9px;font-weight:600;display:flex;align-items:center;justify-content:center}

.footer{left:0;top:1133px;width:650px;height:67px;background:var(--footer);border-top:2px solid #4f7a22;color:#cfdcbf;font-size:8.5px;line-height:13px;text-align:center;padding-top:17px}
</style>
</head>
<body>
<div class="page">
  <header>
    <div class="abs brand"><span class="brand-dot"></span><span class="brand-name">LEAFMORE ENERGY</span></div>
    <div class="abs social" aria-label="Social links">
      <span class="s1" role="img" aria-label="Social network"></span>
      <span class="s2" role="img" aria-label="Social network"></span>
      <span class="s3" role="img" aria-label="Social network"></span>
      <span class="divider"></span>
    </div>
    <div class="abs search">Search...
      <svg width="12" height="12" viewBox="0 0 12 12"><circle cx="7" cy="5" r="3.8" fill="none" stroke="#6a9a30" stroke-width="1.4"/><line x1="4.2" y1="7.8" x2="1" y2="11" stroke="#6a9a30" stroke-width="1.6"/></svg>
    </div>
    <nav class="abs nav">
      <a class="active" style="width:83px">Home</a>
      <a style="width:90px">About Us</a>
      <a style="width:97px">Blue Pact</a>
      <a style="width:119px">Eco Landlords</a>
      <a style="width:102px">Renewables</a>
      <a style="flex:1">Contact Us</a>
    </nav>
  </header>

  <section class="abs hero" role="img" aria-label="Installers in hard hats fitting solar panels on a tiled roof">
    <h1><em>Welcomes</em> Installers</h1>
    <p>Lets join the most reputed corporates<br>and expand your business profile.</p>
    <span class="join">Join Now</span>
  </section>

  <section class="abs audiences">
    <div class="aud consumers"><h3>Consumers</h3><p>Lorem ipsum dolor sit amet, consectetur adipisicing elit tempor.</p><span class="details">DETAILS</span></div>
    <div class="aud businesses"><h3>Businesses</h3><p>Lorem ipsum dolor sit amet, consectetur adipisicing elit tempor.</p><span class="details">DETAILS</span></div>
    <div class="aud public"><h3>Public Sector</h3><p>Lorem ipsum dolor sit amet, consectetur adipisicing elit tempor.</p><span class="details">DETAILS</span></div>
    <div class="aud installers"><h3>Installers</h3><p>Lorem ipsum dolor sit amet, consectetur adipisicing elit tempor.</p><span class="details">DETAILS</span></div>
  </section>

  <h2 class="abs section-title" style="top:539px;font-weight:400">About Us</h2>
  <svg class="abs about-badge" width="48" height="62" viewBox="0 0 48 62" role="img" aria-label="Accreditation badge">
    <rect x="6" y="4" width="36" height="52" rx="3" fill="#3d7a1a"/>
  </svg>
  <p class="abs about-text">We're a UK based energy efficiency business. We arrange for energy efficient systems to be fitted in people's houses (i.e. efficient boilers, solar panels etc.) However, we do not install them ourselves as we have accredited installers who install on our behalf. Therefore the website should appeal to these businesses and have a very professional corporate feel. The final design should communicate that we are a financially safe large corporation.</p>

  <section class="abs products">
    <h2 class="abs section-title" style="top:23px;font-weight:400">Our Products</h2>
    <span class="abs arrow" style="left:50px;top:110px">&#8249;</span>
    <span class="abs arrow" style="left:592px;top:110px">&#8250;</span>
    <div class="abs product" style="left:88px;top:56px">
      <h4>Corvane Boilers</h4>
      <div class="thumb"><div role="img" aria-label="White wall-mounted boiler" style="background:linear-gradient(90deg,#17475f,#3f6f86 45%,#d9e2e6 60%,#5d8aa0)"></div></div>
      <p>Lorem ipsum dolor sit upoe amet, consectetur adipisicing elit, sed do eiusmod tempor.</p>
      <span class="more">Read More</span>
    </div>
    <div class="abs product" style="left:252px;top:56px">
      <h4>Solar Panels</h4>
      <div class="thumb"><div role="img" aria-label="Worker installing solar panels under blue sky" style="background:linear-gradient(#4f8fd6,#a9c9ec 45%,#24417a 70%,#1a2d5a)"></div></div>
      <p>Lorem ipsum dolor sit upoe amet, consectetur adipisicing elit, sed do eiusmod tempor.</p>
      <span class="more">Read More</span>
    </div>
    <div class="abs product" style="left:416px;top:56px">
      <h4>Solid Wall Insulation</h4>
      <div class="thumb"><div role="img" aria-label="Worker applying insulation to a wall" style="background:linear-gradient(90deg,#8a7a66,#c8b9a4 45%,#e8e6e3 70%,#bdbdbd)"></div></div>
      <p>Lorem ipsum dolor sit upoe amet, consectetur adipisicing elit, sed do eiusmod tempor.</p>
      <span class="more">Read More</span>
    </div>
  </section>

  <h2 class="abs block-title" style="left:89px;top:934px"><em>Clients</em> Testimonials</h2>
  <div class="abs avatar" role="img" aria-label="Portrait of a client in a suit"></div>
  <p class="abs who"><b>Daniel Hartley</b><br>Brookfield Housing Estate<br>New Zealand</p>
  <p class="abs quote">Lorem ipsum dolor sit amet, consectetur adipisicing elit, sed do eiusmod tempor incididunt ut labore et dolore magna aliqua.</p>

  <h2 class="abs block-title" style="left:347px;top:934px"><em>Quick</em> Contact</h2>
  <div class="abs field" style="top:961px;height:23px">Your Name</div>
  <div class="abs field" style="top:990px;height:23px">Email id</div>
  <div class="abs field" style="top:1019px;height:54px">Query</div>
  <span class="abs submit">Submit</span>

  <footer class="abs footer">COPYRIGHT@2013, LEAFMORE<br>TERMS &amp; POLICY</footer>
</div>
</body>
</html>
```